Bellcrest HVAC Business Card design

Looking for a modern professional two sided design. Showing contact info and services provided. Possibly on a silk card stock.
Using blues or greens or greys and maybe metallic. One color or a mixture of these.
Dorian Vance
dvance@bellcresthvac-example.net
555-318-4702
Air Conditioning
Heating
Heat Pumps / Gas / Oil
Ductless mini splits
Controls
VFD's
Pumps
Gas Fitting/Piping
Service and New install
Residential / Commercial
Industry/Entity Type
Mechanical HVAC
Contact Information for Business Card
Logo, contact info and provided services

```html
<!DOCTYPE html>
<html lang="en">
<head>
<meta charset="utf-8">
<title>Bellcrest HVAC Business Card</title>
<link rel="stylesheet" href="https://fonts.googleapis.com/css2?family=Poppins:wght@400;600&family=Playfair+Display:wght@700&display=swap">
<style>
  :root {
    --stage: #2e2826;
    --card: #1b1b1b;
    --silver: #e3e4e4;
    --silver-dark: #9a9c9c;
    --ink-light: #f2f2f2;
  }
  * { margin: 0; padding: 0; box-sizing: border-box; }
  html, body { width: 1200px; height: 842px; overflow: hidden; }
  body {
    background: var(--stage);
    font-family: "Poppins", sans-serif;
    position: relative;
  }
  .card {
    position: absolute;
    top: 266px;
    width: 540px;
    height: 309px;
    background: var(--card);
    overflow: hidden;
    box-shadow: 0 10px 30px rgba(0,0,0,.45);
  }
  .card--info { left: 40px; }
  .card--brand { left: 620px; }

  /* info side */
  .band {
    position: absolute;
    left: 0; right: 0;
    height: 13px;
    background: var(--silver);
  }
  .band--top { top: 20px; }
  .band--bottom { bottom: 20px; }
  .name-badge {
    position: absolute;
    left: 50%;
    top: 48px;
    transform: translateX(-50%);
    width: 176px;
    height: 68px;
    border: 3px solid var(--silver-dark);
    border-radius: 50%;
    display: flex;
    align-items: center;
    justify-content: center;
  }
  .name-badge__text {
    font-family: "Playfair Display", serif;
    font-weight: 700;
    font-size: 15px;
    letter-spacing: .5px;
    text-transform: uppercase;
    color: var(--ink-light);
  }
  .contact {
    position: absolute;
    top: 136px;
    display: flex;
    align-items: center;
    gap: 7px;
    color: var(--ink-light);
    font-size: 14.5px;
    letter-spacing: .3px;
  }
  .contact--phone { left: 40px; }
  .contact--email { right: 30px; font-size: 13.5px; }
  .contact svg { width: 16px; height: 16px; fill: var(--ink-light); }
  .services {
    position: absolute;
    left: 0; right: 0;
    top: 176px;
    text-align: center;
    color: var(--ink-light);
    font-size: 15px;
    line-height: 22px;
    letter-spacing: .2px;
  }

  /* brand side */
  .accent {
    position: absolute;
    width: 30px;
    height: 78px;
    display: flex;
    gap: 5px;
  }
  .accent__bar { width: 20px; height: 100%; background: var(--silver); }
  .accent__line { width: 4px; height: 100%; background: var(--silver-dark); }
  .accent--top { top: 28px; right: 26px; flex-direction: row-reverse; }
  .accent--bottom { bottom: 28px; left: 26px; }
  .brand-mark {
    position: absolute;
    left: 50%;
    top: 50%;
    transform: translate(-50%, -50%);
    display: flex;
    align-items: center;
    gap: 14px;
  }
  .brand-mark__dot {
    width: 22px; height: 22px;
    border-radius: 50%;
    background: var(--silver);
  }
  .brand-mark__name {
    font-family: "Poppins", sans-serif;
    font-weight: 600;
    font-size: 30px;
    letter-spacing: 1px;
    text-transform: uppercase;
    color: var(--silver);
  }
</style>
</head>
<body>
  <section class="card card--info" aria-label="Contact side">
    <div class="band band--top"></div>
    <div class="name-badge"><span class="name-badge__text">Dorian Vance</span></div>
    <div class="contact contact--phone">
      <svg viewBox="0 0 24 24" aria-hidden="true"><path d="M6.6 10.8a15.1 15.1 0 0 0 6.6 6.6l2.2-2.2c.3-.3.7-.4 1-.2 1.1.4 2.3.6 3.6.6.6 0 1 .4 1 1V20c0 .6-.4 1-1 1A17 17 0 0 1 3 4c0-.6.4-1 1-1h3.5c.6 0 1 .4 1 1 0 1.3.2 2.5.6 3.6.1.3 0 .7-.2 1z"/></svg>
      <span>555-318-4702</span>
    </div>
    <div class="contact contact--email">
      <svg viewBox="0 0 24 24" aria-hidden="true"><path d="M2 5h20v14H2zm2 2v.4l8 5.2 8-5.2V7zm0 2.8V17h16V9.8l-8 5.2z"/></svg>
      <span>dvance@bellcresthvac-example.net</span>
    </div>
    <div class="services">
      <p>Air Conditioning • Heating • Heat Pumps / Gas / Oil</p>
      <p>Ductless mini splits • Controls • VFD's • Pumps</p>
      <p>Gas Fitting/Piping • Service and New install</p>
      <p>Residential / Commercial</p>
    </div>
    <div class="band band--bottom"></div>
  </section>

  <section class="card card--brand" aria-label="Brand side">
    <div class="accent accent--top"><span class="accent__bar"></span><span class="accent__line"></span></div>
    <div class="brand-mark">
      <span class="brand-mark__dot"></span>
      <span class="brand-mark__name">Bellcrest HVAC</span>
    </div>
    <div class="accent accent--bottom"><span class="accent__bar"></span><span class="accent__line"></span></div>
  </section>
</body>
</html>
```